LEARN Business Skills so you can Earn a good living

size of the poster is 8”x 10.75" plus 0.25" bleed.
Please leave 1 inch on the bottoum for footer
I want a design a poster that will attract people's attention.
I appreciate a creative ad however the ad should not take away from being able to clearly read the text.
-I also appreciate a simple creative ad that is not too busy.
-you can use graphics, vectors, or pictures of real people.
-however, if you use real people it should be a white male that is wearing a white shirt and look like a professional person.

Target Market(s)

Potential young business people

Industry/Entity Type

education

Requirements
Must have
• easy to read the text
Nice to have
• I would like a "creative" simple ad that is easy to be read
Should not have
• pictures of women

```html
<!DOCTYPE html>
<html lang="en">
<head>
<meta charset="utf-8">
<title>Business Enrichment Course</title>
<link rel="stylesheet" href="https://fonts.googleapis.com/css2?family=Bebas+Neue&family=Hind:wght@400&family=Montserrat:wght@700&family=Questrial&display=swap">
<style>
  :root {
    --navy: #07073f;
    --orange: #f77f0e;
    --orange-deep: #ff4a1c;
    --white: #ffffff;
    --rule: #8a8aa8;
    --photo-light: #d9dcd8;
    --photo-mid: #a9b3ad;
    --figure-tone: #1c1c5a;
  }
  * { margin: 0; padding: 0; box-sizing: border-box; }
  html, body { width: 907px; height: 1200px; overflow: hidden; background: var(--navy); }
  .poster { position: relative; width: 907px; height: 1200px; background: var(--navy); overflow: hidden; color: var(--white); }
  .backdrop { position: absolute; inset: 0; width: 907px; height: 1200px; }

  .brand { position: absolute; left: 45px; top: 62px; display: flex; align-items: center; gap: 24px; }
  .brand-mark { width: 66px; height: 66px; border: 3px solid var(--white); border-radius: 50%; flex: none; }
  .brand-name { font-family: "Montserrat", sans-serif; font-weight: 700; font-size: 44px; line-height: 52px; color: var(--white); }

  .frame-corner { position: absolute; border-color: var(--white); border-style: solid; }
  .frame-corner.top { left: 57px; top: 249px; width: 62px; height: 65px; border-width: 3px 0 0 3px; }
  .frame-corner.bottom { left: 317px; top: 509px; width: 62px; height: 65px; border-width: 0 3px 3px 0; }

  .title { position: absolute; left: 79px; top: 262px; font-family: "Bebas Neue", sans-serif; font-size: 97px; line-height: 103px; letter-spacing: 0.075em; color: var(--orange); }

  .tagline { position: absolute; left: 69px; top: 589px; width: 384px; height: 78px; border-top: 1px solid var(--rule); border-bottom: 1px solid var(--rule); padding: 8px 0 0 18px; font-family: "Bebas Neue", sans-serif; font-size: 34px; line-height: 32px; letter-spacing: 0.01em; }

  .skills-heading { position: absolute; left: 87px; top: 682px; font-family: "Hind", sans-serif; font-size: 26px; line-height: 30px; letter-spacing: 0.02em; }
  .benefits { position: absolute; left: 91px; top: 716px; list-style: none; font-family: "Questrial", sans-serif; font-size: 22px; }
  .benefits li { display: flex; align-items: center; height: 29.5px; }
  .benefits svg { width: 24px; height: 24px; margin-right: 43px; flex: none; }

  .topics { position: absolute; left: 223px; top: 821px; width: 503px; height: 224px; border: 2px solid var(--orange); padding: 9px 15px 0 14px; font-family: "Questrial", sans-serif; font-size: 17.5px; line-height: 21.4px; text-align: justify; text-transform: uppercase; }

  .photo { position: absolute; border-radius: 50%; border: 9px solid var(--white); }
  .photo-one { left: 501px; top: 46px; width: 310px; height: 310px; background: linear-gradient(135deg, var(--photo-mid), var(--photo-light)); }
  .photo-two { left: 578px; top: 312px; width: 288px; height: 288px; background: linear-gradient(160deg, var(--photo-light), #c8c8c8); }
  .photo-three { left: 624px; top: 553px; width: 244px; height: 244px; background: linear-gradient(135deg, #b9c6c2, var(--photo-light)); }
  .presenter { position: absolute; left: 743px; top: 827px; width: 104px; height: 226px; background: var(--figure-tone); border-radius: 8px; }
</style>
</head>
<body>
<div class="poster">
  <svg class="backdrop" viewBox="0 0 1672 2212" preserveAspectRatio="none" aria-hidden="true">
    <defs>
      <linearGradient id="band" x1="0" y1="0" x2="1" y2="0">
        <stop offset="0" stop-color="#ff8a0a"/>
        <stop offset="1" stop-color="#ff4a1c"/>
      </linearGradient>
      <linearGradient id="bandRight" x1="0" y1="0" x2="1" y2="0">
        <stop offset="0" stop-color="#ff4a1c"/>
        <stop offset="1" stop-color="#ff8a0a"/>
      </linearGradient>
    </defs>
    <polygon points="1255,0 1520,0 1170,350 905,350" fill="url(#bandRight)"/>
    <polygon points="1420,320 1650,550 1672,572 1672,860 1430,1100 1300,1100 1640,710 1330,400" fill="url(#band)"/>
    <polygon points="1360,1400 1560,1400 1672,1512 1672,1760" fill="url(#band)"/>
    <polygon points="0,1430 340,1745 340,1890 18,2212 0,2212 0,2060 255,1815 0,1580" fill="url(#band)"/>
  </svg>

  <div class="brand">
    <span class="brand-mark"></span>
    <div class="brand-name">SKILL<br>to<br>THRIVE</div>
  </div>

  <span class="frame-corner top"></span>
  <span class="frame-corner bottom"></span>
  <h1 class="title">BUSINESS<br>ENRICHMENT<br>COURSE</h1>

  <p class="tagline">A PROVEN SUCCESS OF HELPING<br>PEOPLE IN THEIR LIVELIHOODS</p>

  <h2 class="skills-heading">BUSINESS SKILLS THAT WILL HELP YOU:</h2>
  <ul class="benefits">
    <li><svg viewBox="0 0 24 24" aria-hidden="true"><circle cx="12" cy="12" r="12" fill="#f77f0e"/><rect x="6" y="9" width="12" height="9" fill="#fff"/><rect x="10" y="6.5" width="4" height="3" fill="none" stroke="#fff" stroke-width="1.4"/></svg>Get A Quality Job</li>
    <li><svg viewBox="0 0 24 24" aria-hidden="true"><circle cx="12" cy="12" r="12" fill="#f77f0e"/><rect x="6" y="14" width="2.5" height="4" fill="#fff"/><rect x="10" y="12" width="2.5" height="6" fill="#fff"/><rect x="14" y="10" width="2.5" height="8" fill="#fff"/><path d="M6 11 L16 5 M13 5 H16 V8" stroke="#fff" stroke-width="1.4" fill="none"/></svg>Start/Grow Your Business</li>
    <li><svg viewBox="0 0 24 24" aria-hidden="true"><circle cx="12" cy="12" r="12" fill="#f77f0e"/><circle cx="10" cy="9" r="3" fill="#fff"/><path d="M4.5 18 Q10 10 15.5 18 Z" fill="#fff"/><path d="M17 14 V6 M15 8 L17 6 L19 8" stroke="#fff" stroke-width="1.4" fill="none"/></svg>Increase Your Salary</li>
  </ul>

  <p class="topics">Business Admiistration - Small Business Management - Finance - Investments - Computers- Accounting - Sales Marketing - Project Management Interviewing Skills - Business Law - Negotiation - Public Speaking - Import/Export - Information Technoloy - Distribution - Marketing - Ledgerly - Real Estate - Health Care - Management - Shopnest</p>

  <div class="photo photo-one" role="img" aria-label="Photo of a professional man in a white shirt with arms crossed"></div>
  <div class="photo photo-two" role="img" aria-label="Photo of a smiling professional man in a white shirt giving a thumbs up"></div>
  <div class="photo photo-three" role="img" aria-label="Photo of a professional man in a white shirt and tie with arms crossed"></div>
  <div class="presenter" role="img" aria-label="Illustration of a businessman presenting with a pointer"></div>
</div>
</body>
</html>
```